I sell Finches---picture of White Finch Bird----

I raise and sell light color and white Finch - need card to give to Pet shops with my name - Dora Pelkey, address: 271 North Corwen St. Alder Cove, Ca. 95021 - phone - 555-417-3968. All birds raised and nourished in large outside aviary--very healthy and cared for. Would like card to be shiny red with bold print in Broadway font----purple bold print on red card. Design options open - you know best. Would like a picture or pictures of Finches - light or white in color.

THE WREN KEEPER (LARGE, BOLD BROADWAY PRINT)

```html
<!DOCTYPE html>
<html lang="en">
<head>
<meta charset="utf-8">
<title>The Wren Keeper – Business Card</title>
<link rel="stylesheet" href="https://fonts.googleapis.com/css2?family=Barlow:wght@600&family=Limelight&family=Indie+Flower&family=Roboto:wght@400&display=swap">
<style>
  :root {
    --page-bg: #262626;
    --card-red: #ee1c25;
    --card-magenta: #b3296a;
    --card-purple: #5b2d91;
    --stripe-white: #ffffff;
    --stripe-purple: #5b3a97;
    --stripe-red: #e8202a;
    --photo-warm: #8c6d4c;
    --photo-dark: #17120e;
    --text-white: #ffffff;
    --icon-purple: #6a2f8f;
  }
  * { box-sizing: border-box; margin: 0; padding: 0; }
  html, body {
    width: 915px;
    height: 1200px;
    overflow: hidden;
    background: var(--page-bg);
  }
  .canvas {
    position: relative;
    width: 915px;
    height: 1200px;
  }
  .business-card {
    position: absolute;
    left: 40px;
    top: 356px;
    width: 835px;
    height: 488px;
    overflow: hidden;
    background: linear-gradient(180deg, var(--card-red) 0%, var(--card-red) 25%, var(--card-magenta) 58%, var(--card-purple) 100%);
    box-shadow: 0 6px 18px rgba(0,0,0,0.45);
    color: var(--text-white);
  }
  .card-art {
    position: absolute;
    inset: 0;
    width: 835px;
    height: 488px;
  }
  .owner-name {
    position: absolute;
    left: 46px;
    top: 72px;
    font-family: "Barlow", Arial, sans-serif;
    font-weight: 600;
    font-size: 28px;
    letter-spacing: 0.5px;
    line-height: 1;
  }
  .business-name {
    position: absolute;
    left: 40px;
    top: 182px;
    font-family: "Limelight", Georgia, serif;
    font-weight: 400;
    font-size: 50px;
    line-height: 1;
    letter-spacing: -0.5px;
    white-space: nowrap;
  }
  .tagline {
    position: absolute;
    left: 42px;
    top: 238px;
    width: 480px;
    font-family: "Indie Flower", cursive;
    font-size: 22px;
    line-height: 31px;
  }
  .contact {
    position: absolute;
    top: 347px;
    display: flex;
    align-items: flex-start;
    gap: 10px;
    font-family: "Roboto", Arial, sans-serif;
    font-size: 23px;
    line-height: 29px;
  }
  .contact--phone { left: 45px; }
  .contact--address { left: 269px; }
  .contact-text { font-style: normal; }
  .contact-icon {
    flex: none;
    width: 30px;
    height: 30px;
  }
</style>
</head>
<body>
<main class="canvas">
  <section class="business-card">
    <svg class="card-art" viewBox="0 0 723 423" preserveAspectRatio="none">
      <defs>
        <linearGradient id="photoTone" x1="0" y1="0" x2="0" y2="1">
          <stop offset="0" stop-color="#8c6d4c"/>
          <stop offset="0.45" stop-color="#3a2c20"/>
          <stop offset="1" stop-color="#17120e"/>
        </linearGradient>
      </defs>
      <path class="swoosh swoosh--white-outer" fill="var(--stripe-white)" d="M474,0 C440,150 470,330 614,423 L723,423 L723,0 Z"/>
      <path class="swoosh swoosh--purple" fill="var(--stripe-purple)" d="M484,0 C456,155 488,330 618,423 L723,423 L723,0 Z"/>
      <path class="swoosh swoosh--white-inner" fill="var(--stripe-white)" d="M542,0 C508,160 522,330 622,423 L723,423 L723,0 Z"/>
      <path class="swoosh swoosh--red" fill="var(--stripe-red)" d="M554,0 C520,165 532,330 626,423 L723,423 L723,0 Z"/>
      <g role="img" aria-label="Photo of a white finch perched on a branch">
        <path class="finch-photo" fill="url(#photoTone)" d="M564,0 C530,170 540,330 630,423 L723,423 L723,0 Z"/>
      </g>
    </svg>

    <p class="owner-name">DORA PELKEY</p>
    <h1 class="business-name">THE WREN KEEPER</h1>
    <p class="tagline">All birds raised and nourished in large outside aviary<br>– very healthy and cared for.</p>

    <div class="contact contact--phone">
      <svg class="contact-icon" viewBox="0 0 30 30" aria-hidden="true">
        <circle cx="15" cy="15" r="14" fill="var(--text-white)"/>
        <rect x="10" y="7" width="10" height="16" rx="2" fill="var(--icon-purple)"/>
        <rect x="11.8" y="9.5" width="6.4" height="9.5" fill="var(--text-white)"/>
        <circle cx="15" cy="21" r="1" fill="var(--text-white)"/>
      </svg>
      <span class="contact-text">555-417-3968</span>
    </div>

    <div class="contact contact--address">
      <svg class="contact-icon" viewBox="0 0 30 30" aria-hidden="true">
        <circle cx="15" cy="15" r="14" fill="var(--text-white)"/>
        <path d="M15,6 C11,6 8.5,9 8.5,12.5 C8.5,17 15,24 15,24 C15,24 21.5,17 21.5,12.5 C21.5,9 19,6 15,6 Z" fill="var(--icon-purple)"/>
        <circle cx="15" cy="12.5" r="2.6" fill="var(--text-white)"/>
      </svg>
      <address class="contact-text">271 North Corwen<br>St. Alder Cove,<br>Ca. 95021</address>
    </div>
  </section>
</main>
</body>
</html>
```